Fun relaxed Travel Photography Business Card*

Require a fun, funky and quirky but rememberable business card for a travel photographer

Industry/Entity Type

Photographer

Contact Information for Business Card

Front Card

(my name) Tavo M.

Travel Photographer ( small under travel photographer) “self-proclaimed”

(website logo) wanderingtavo.example

(Instagram logo) @wandering_with_tavo

(Instagram logo) @wandering_with_tavo_2.0 (backup for when Instagram puts Tavo on timeout for bad behaviour)

Tel: N/A (removing the potential awkwardness of me not replying)

Email: (see above)

Back Card

Offending people since 1986

(Bottom right corner) “p.s. travelling made me fatTER”

Font styles to use
Serif

Colors

Designer to choose colors to be used in the design.

Requirements
Must have
• a camera
• a similar cartoon version of me as the "logo" see attached files, try to make as similar as possible

```html
<!DOCTYPE html>
<html lang="en">
<head>
<meta charset="utf-8">
<title>Tavo M. – Travel Photographer Business Card</title>
<link rel="stylesheet" href="https://fonts.googleapis.com/css2?family=Lato:wght@400;700&family=Marcellus+SC&display=swap">
<style>
  :root {
    --backdrop: #2a2a2a;
    --card: #0a0a0b;
    --ink-strong: #ffffff;
    --ink-soft: #8c8c8c;
    --ink-dim: #6f6f6f;
    --deco: #1b1b1c;
    --tan-light: #c98a52;
    --tan-dark: #8a4a22;
  }
  * { box-sizing: border-box; margin: 0; padding: 0; }
  html, body { width: 1200px; height: 1108px; overflow: hidden; }
  body {
    background: var(--backdrop);
    display: flex;
    align-items: center;
    justify-content: center;
    gap: 60px;
    font-family: "Lato", sans-serif;
  }
  .card {
    position: relative;
    width: 500px;
    height: 800px;
    background: var(--card);
    border-radius: 28px;
    overflow: hidden;
  }

  /* Front */
  .brand-mark {
    position: absolute;
    left: 40px;
    right: 40px;
    top: 110px;
    height: 260px;
    display: flex;
    flex-direction: column;
    align-items: center;
    justify-content: center;
    gap: 24px;
  }
  .brand-mark__dot {
    width: 150px;
    height: 150px;
    border-radius: 50%;
    background: var(--deco);
  }
  .brand-mark__name {
    font-weight: 700;
    font-size: 42px;
    color: var(--deco);
    letter-spacing: 1px;
  }
  .identity {
    position: absolute;
    left: 70px;
    top: 440px;
  }
  .identity__name {
    font-weight: 700;
    font-size: 46px;
    color: var(--ink-strong);
    line-height: 1.1;
  }
  .identity__role {
    font-size: 27px;
    color: var(--ink-dim);
    margin-top: 4px;
  }
  .identity__note {
    font-size: 20px;
    color: var(--ink-dim);
  }
  .contacts {
    position: absolute;
    left: 60px;
    top: 600px;
    list-style: none;
  }
  .contacts__item {
    display: flex;
    align-items: center;
    gap: 14px;
    font-size: 25px;
    color: var(--ink-soft);
    line-height: 36px;
  }
  .contacts__item--plain { padding-left: 36px; }
  .contacts__icon { width: 22px; height: 22px; flex: none; }

  /* Back */
  .slogan {
    position: absolute;
    top: 110px;
    left: 0;
    right: 0;
    text-align: center;
    font-family: "Marcellus SC", serif;
    font-weight: 400;
    font-size: 36px;
    line-height: 1.15;
    letter-spacing: 3px;
    color: var(--ink-strong);
  }
  .mascot {
    position: absolute;
    left: 95px;
    top: 380px;
    width: 320px;
    height: 250px;
    border-radius: 24px;
    background: linear-gradient(160deg, var(--tan-light), var(--tan-dark));
    opacity: 0.85;
  }
  .postscript {
    position: absolute;
    bottom: 70px;
    left: 0;
    right: 0;
    text-align: center;
    font-size: 26px;
    color: var(--ink-soft);
  }
</style>
</head>
<body>
  <section class="card card--front">
    <div class="brand-mark">
      <span class="brand-mark__dot"></span>
      <span class="brand-mark__name">wanderingtavo</span>
    </div>
    <div class="identity">
      <h1 class="identity__name">Tavo M.</h1>
      <p class="identity__role">Travel Photographer</p>
      <p class="identity__note">self-proclaimed</p>
    </div>
    <ul class="contacts">
      <li class="contacts__item">
        <svg class="contacts__icon" viewBox="0 0 24 24" fill="none" stroke="#fff" stroke-width="2.4" stroke-linecap="round" stroke-linejoin="round"><path d="M5 3h4l2 5-3 2a12 12 0 0 0 6 6l2-3 5 2v4a2 2 0 0 1-2 2A17 17 0 0 1 3 5a2 2 0 0 1 2-2z"/></svg>
        555 0142 386
      </li>
      <li class="contacts__item">
        <svg class="contacts__icon" viewBox="0 0 24 24" fill="#fff"><path d="M2 5h20v14H2z"/><path d="M2 5l10 8 10-8" fill="none" stroke="#0a0a0b" stroke-width="2"/></svg>
        info@wanderingtavo.example
      </li>
      <li class="contacts__item">
        <svg class="contacts__icon" viewBox="0 0 24 24" fill="none" stroke="#fff" stroke-width="1.8"><circle cx="12" cy="12" r="10"/><path d="M2 12h20M12 2c3 3 3 17 0 20M12 2c-3 3-3 17 0 20"/></svg>
        wanderingtavo.example
      </li>
      <li class="contacts__item">
        <svg class="contacts__icon" viewBox="0 0 24 24"><rect x="2" y="2" width="20" height="20" rx="4" fill="#fff"/></svg>
        @wandering_with_tavo
      </li>
      <li class="contacts__item contacts__item--plain">@wandering_with_tavo_2.0</li>
    </ul>
  </section>

  <section class="card card--back">
    <h2 class="slogan">Offending people<br>since 1986</h2>
    <div class="mascot" role="img" aria-label="Cartoon mascot of the photographer relaxing on a wooden sun lounger"></div>
    <p class="postscript">p.s. travelling made me fatTER</p>
  </section>
</body>
</html>
```